Brochure flyer for handout and web distribution - 11 X 17 folded four pages 8.5 X 11

We need a brochure for trade shows. Title page is "When Speed To Market Counts - We Deliver"- company logos on bottom of the page.

We build cannabis grow facilities and can build 3-6 months faster than conventional building methods. We want to use green as a focus color. We have an image cannabis interactive that we want to have in the center fold. It comes from this webpage which has the building descriptions - https://www.tallowfen.com/cannabis-buildings

Also attached is an ad from Hempvora we did for a previous show that shows how I would like logos on the back cover - without the background image and without the text - replace text on back page with file attached with key advantages that we would like on the back page as well.

There are also some images from our partner MeltaBrook that we would love to show on the inside cover as well - so one page is Brevik interactive and buildings and the other inside page features MeltaBrook.

For content on Melta-Brook - When choosing between modular construction and traditionally constructed rooms, consider that all modular construction is objectively faster and more affordable. On average you can cut construction time by half when using a modular room and building design compared to conventionally construction. All components used to construct modular rooms and buildings have already been designed and fabricated at our plant, causing:
• Less disruption to your daily business operations
• Less construction waste and debris
Logos are attached for the back page - these can also be used on the front page. Website is www.rivenstalkworks.com (visit us). Contact us at info@rivenstalkworks.com

All images can be provided EPS - final design will need to be 300DPI minimum

Target Market(s)

Lead investors in Cannabis

Industry/Entity Type

Cannabis Industry

Font styles to use
Serif

Colors
0094D4
00A9DD
6FCCEA
C7EBF8
E9F6FB
00AB8E
00BBA5
67D7C9
C6EFE9
E9F9F6

Requirements
Must have
• Logos, website, 4 pages
Should not have
• Cannabis images

```html
<!DOCTYPE html>
<html lang="en">
<head>
<meta charset="utf-8">
<title>Korvane Partners Trade Show Brochure</title>
<link rel="stylesheet" href="https://fonts.googleapis.com/css2?family=Oswald:wght@500;600&family=Open+Sans:wght@400;600;700&display=swap">
<style>
  :root {
    --green: #6cbe3b;
    --green-deep: #3f8f2a;
    --green-soft: #8fd05e;
    --charcoal: #3a3d40;
    --ink: #2b2b2b;
    --text: #555b5f;
    --paper: #ffffff;
    --backdrop: #e4e5e6;
  }
  * { box-sizing: border-box; margin: 0; padding: 0; }
  html, body { width: 800px; height: 1200px; overflow: hidden; }
  body { background: var(--backdrop); font-family: "Open Sans", sans-serif; color: var(--text); position: relative; }

  /* ---------- Front cover ---------- */
  .cover { position: absolute; left: 170px; top: 70px; width: 460px; height: 460px; background: var(--paper); overflow: hidden; box-shadow: 0 6px 18px rgba(0,0,0,.18); }
  .cover-shapes { position: absolute; inset: 0; }
  .cover-headline { position: absolute; left: 36px; top: 296px; font-family: "Oswald", sans-serif; font-weight: 500; font-size: 17px; line-height: 1.25; color: var(--paper); text-transform: uppercase; letter-spacing: .2px; }
  .cover-web { position: absolute; left: 36px; top: 350px; font-size: 8px; font-weight: 600; color: var(--paper); display: flex; align-items: center; gap: 5px; }
  .cover-web .dot { width: 8px; height: 8px; border-radius: 50%; background: var(--paper); }
  .brand { position: absolute; right: 16px; top: 250px; width: 140px; text-align: right; }
  .brand-mark { width: 36px; height: 36px; background: var(--ink); margin: 0 36px 8px auto; }
  .brand-name { font-weight: 700; font-size: 16px; color: var(--ink); line-height: 1; white-space: nowrap; }
  .brand-tag { font-size: 6.5px; color: var(--text); margin-top: 4px; white-space: nowrap; }

  /* ---------- Inside spread ---------- */
  .spread { position: absolute; left: 20px; top: 700px; width: 760px; height: 380px; display: flex; box-shadow: 0 6px 18px rgba(0,0,0,.18); }
  .page { position: relative; width: 380px; height: 380px; background: var(--paper); overflow: hidden; }
  .page-rule { position: absolute; left: 0; right: 0; bottom: 8px; height: 5px; background: var(--green); }

  .site-plan { position: absolute; left: 0; top: 14px; width: 380px; height: 140px; background: linear-gradient(160deg, #3d6a36 0%, #6f8d5a 45%, #b7bcb4 70%, #5a7d45 100%); }
  .corner-accent { position: absolute; left: 0; top: 0; }
  .section-title { font-family: "Oswald", sans-serif; font-weight: 600; text-transform: uppercase; color: var(--ink); }
  .left-title { position: absolute; left: 18px; top: 162px; font-size: 15px; }
  .left-intro { position: absolute; left: 18px; top: 185px; width: 344px; font-size: 6px; line-height: 1.45; }
  .building-list { position: absolute; left: 18px; top: 218px; width: 344px; list-style: none; display: grid; grid-template-columns: 1fr 1fr; column-gap: 18px; row-gap: 5px; grid-auto-flow: column; grid-template-rows: repeat(4, auto); }
  .building-list li { display: flex; gap: 6px; font-size: 5.6px; line-height: 1.4; }
  .num { flex: none; width: 10px; height: 10px; border-radius: 50%; background: var(--green); color: var(--paper); font-size: 6px; font-weight: 700; display: flex; align-items: center; justify-content: center; }
  .building-list strong { display: block; color: var(--ink); font-size: 6.2px; }

  .feature-band { position: absolute; left: 0; top: 0; width: 380px; height: 150px; background: linear-gradient(180deg, var(--green-soft), var(--green)); }
  .right-title { position: absolute; left: 0; right: 0; top: 24px; text-align: center; font-size: 14px; color: var(--paper); }
  .right-intro { position: absolute; left: 40px; right: 40px; top: 50px; text-align: center; font-size: 6px; line-height: 1.45; color: var(--paper); }
  .room-shots { position: absolute; left: 20px; top: 102px; width: 340px; display: flex; gap: 8px; }
  .room-shot { flex: 1; height: 84px; border: 3px solid var(--paper); box-shadow: 0 1px 4px rgba(0,0,0,.2); }
  .shot-panel { background: linear-gradient(135deg, #f3f3f3, #cfd0d1); }
  .shot-booth { background: linear-gradient(180deg, #8db9d6 0%, #b9c4ca 50%, #6f8a5a 100%); }
  .shot-room { background: linear-gradient(135deg, #e8e8e8, #a9abad); }
  .modular-copy { position: absolute; left: 20px; top: 196px; width: 340px; font-size: 6px; line-height: 1.45; }
  .modular-copy p { margin-bottom: 5px; }
  .benefits { position: absolute; left: 20px; top: 260px; list-style: none; }
  .benefits li { display: flex; align-items: center; gap: 6px; font-size: 6.4px; font-weight: 700; color: var(--ink); margin-bottom: 6px; }
  .benefit-icon { width: 14px; height: 14px; border-radius: 50%; background: var(--charcoal); display: flex; align-items: center; justify-content: center; }
  .grow-room { position: absolute; right: 18px; bottom: 20px; width: 140px; height: 84px; background: linear-gradient(180deg, #6b6452 0%, #b89a5c 40%, #3f5a3a 100%); }
  .corner-dark { position: absolute; right: 0; bottom: 0; }
</style>
</head>
<body>

<section class="cover" aria-label="Front cover">
  <svg class="cover-shapes" width="460" height="460" viewBox="0 0 460 460">
    <defs>
      <linearGradient id="leaf-tone" x1="0" y1="0" x2="1" y2="1">
        <stop offset="0" stop-color="#2f5a2a"/>
        <stop offset=".5" stop-color="#1d3a1c"/>
        <stop offset="1" stop-color="#4c8a3c"/>
      </linearGradient>
    </defs>
    <g role="img" aria-label="Close-up photograph of green leaves">
      <polygon points="0,0 460,0 460,180 270,318 0,232" fill="url(#leaf-tone)"/>
    </g>
    <polygon points="0,232 270,318 460,442 0,442" fill="#6cbe3b"/>
    <polygon points="270,318 460,180 460,442" fill="#ffffff"/>
    <rect x="0" y="442" width="460" height="18" fill="#3a3d40"/>
    <rect x="0" y="452" width="460" height="4" fill="#6cbe3b"/>
  </svg>
  <h1 class="cover-headline">When speed to<br>market counts - We deliver</h1>
  <p class="cover-web"><span class="dot"></span>www.rivenstalkworks.com</p>
  <div class="brand">
    <div class="brand-mark"></div>
    <p class="brand-name">Korvane Partners</p>
    <p class="brand-tag">Design / Build Advisory Services</p>
  </div>
</section>

<section class="spread" aria-label="Inside spread">
  <article class="page page-left">
    <div class="site-plan" role="img" aria-label="Aerial illustration of a cannabis campus with Brevik structures, greenhouses and solar field"></div>
    <svg class="corner-accent" width="150" height="60" viewBox="0 0 150 60"><polygon points="0,0 150,0 0,60" fill="#6cbe3b"/></svg>
    <h2 class="section-title left-title">Brevik interactive and buildings</h2>
    <p class="left-intro">Brevik structures are the ideal solution for growers, processors and producers of cannabis products. Our versatile structures are engineered to be built virtually anywhere and are perfect for on-site processing. Designed to be relocatable, they can be moved as needs change.</p>
    <ol class="building-list">
      <li><span class="num">1</span><span><strong>Blackout Growing Structures</strong>Complete control over your growing environment in a large space.</span></li>
      <li><span class="num">2</span><span><strong>Greenhouse Growing Structures</strong>A translucent membrane gives optimal light, with a 10 year warranty.</span></li>
      <li><span class="num">3</span><span><strong>On-site Composting</strong>Avoid costs and keep soil healthy by composting on site.</span></li>
      <li><span class="num">4</span><span><strong>Hoop houses</strong>Use your own space to protect your crops while they grow.</span></li>
      <li><span class="num">5</span><span><strong>Processing Facilities</strong>Skip transport to off-site processing with a climate-controlled space.</span></li>
      <li><span class="num">6</span><span><strong>Administration Buildings</strong>Bright buildings with large windows and daylight panels.</span></li>
      <li><span class="num">7</span><span><strong>Retail</strong>Give your customers a welcoming experience in a bright space.</span></li>
      <li><span class="num">8</span><span><strong>Hail Shelters</strong>Protect millions of dollars in crops with hail shelters.</span></li>
    </ol>
    <div class="page-rule"></div>
  </article>

  <article class="page page-right">
    <div class="feature-band"></div>
    <h2 class="section-title right-title">Features MeltaBrook</h2>
    <p class="right-intro">Every business needs to run as efficiently as possible. As one of the most experienced modular construction companies in the world, we're aware of the advantages that modular building offers. From streamlining the building process to more affordable use of space, we offer the perfect solution for saving time and money.</p>
    <div class="room-shots">
      <div class="room-shot shot-panel" role="img" aria-label="Modular wall panel system"></div>
      <div class="room-shot shot-booth" role="img" aria-label="Prefabricated guard booth on site"></div>
      <div class="room-shot shot-room" role="img" aria-label="Rendering of an assembled modular room"></div>
    </div>
    <div class="modular-copy">
      <p>When choosing between modular construction and traditionally constructed rooms, consider that all modular construction is objectively faster and more affordable.</p>
      <p>On average you can cut construction time by half when using a modular room and building design compared to conventionally construction.</p>
      <p>All components used to construct modular rooms and buildings have already been designed and fabricated at our plant, causing:</p>
    </div>
    <ul class="benefits">
      <li><span class="benefit-icon"><svg width="8" height="8" viewBox="0 0 8 8"><path d="M1 4.2 3 6.2 7 1.8" stroke="#6cbe3b" stroke-width="1.4" fill="none"/></svg></span>Less disruption to your daily business operations</li>
      <li><span class="benefit-icon"><svg width="8" height="8" viewBox="0 0 8 8"><path d="M1 4.2 3 6.2 7 1.8" stroke="#6cbe3b" stroke-width="1.4" fill="none"/></svg></span>Less construction waste and debris</li>
    </ul>
    <svg class="corner-dark" width="200" height="60" viewBox="0 0 200 60"><polygon points="200,0 200,60 0,60" fill="#3a3d40"/></svg>
    <div class="grow-room" role="img" aria-label="Cutaway rendering of a modular grow room with plants under lights"></div>
    <div class="page-rule"></div>
  </article>
</section>

</body>
</html>
```